Letterhead and Business card for Construction company

We need a letterhead and business card with our new company logo. We are based in NY. We develop and build properties.

The design should incorporate some unique feature from the logo (shape, font...). it should look like an extension from it.

Design should be clean and elegant, professional, not too busy.

The letterhead should include:
Logo (attached)
Address
Phone
Email

Please find the attached logo images and AI file.

Target Market(s)

Construction industry professionals

Industry/Entity Type

Construction, Development

Font styles to use
Sans Serif

Colors

Designer to choose colors to be used in the design.

Requirements
Must have
• Design should incorporate logo elements, additional assets are welcome. I'd like to see some other shapes / images invorporated too.

```html
<!DOCTYPE html>
<html lang="en">
<head>
<meta charset="utf-8">
<title>Ridgeline Builders Letterhead</title>
<link href="https://fonts.googleapis.com/css2?family=Lato:wght@400&family=Open+Sans:wght@400;700&family=Alex+Brush&display=swap" rel="stylesheet">
<style>
  :root {
    --orange: #f47f20;
    --ink: #231f20;
    --text: #1e1e1e;
    --paper: #ffffff;
    --backdrop: #ffffff;
  }
  * { margin: 0; padding: 0; box-sizing: border-box; }
  html, body { width: 1040px; height: 1200px; overflow: hidden; background: var(--backdrop); }
  .letterhead {
    position: absolute; left: 95px; top: 0;
    width: 849px; height: 1200px;
    background: var(--paper);
    color: var(--text);
  }
  .brand {
    position: absolute; left: 42px; top: 129px;
    display: flex; align-items: center; gap: 10px;
    font-family: "Open Sans", sans-serif; font-weight: 700;
    font-size: 24px; line-height: 34px; color: var(--orange); letter-spacing: 0.5px;
  }
  .brand-mark { width: 16px; height: 16px; background: var(--orange); }
  .contact {
    position: absolute; left: 586px; top: 97px;
    border-left: 1.5px solid var(--orange);
    padding-left: 16px;
    font-family: "Open Sans", sans-serif; font-size: 15.5px; line-height: 21px;
    font-style: normal;
    color: var(--text);
  }
  .contact .address { margin-top: -3px; margin-bottom: 17px; }
  .contact .line { display: flex; align-items: center; gap: 3px; }
  .contact svg { width: 10px; height: 10px; fill: var(--orange); }
  .body-copy {
    position: absolute; left: 42px; top: 420px; width: 764px;
    font-family: "Lato", sans-serif; font-size: 12.9px; line-height: 18.5px;
    text-align: justify;
    hyphens: auto; -webkit-hyphens: auto;
  }
  .body-copy p + p { margin-top: 18.5px; }
  .closing {
    position: absolute; left: 42px; top: 864px;
    font-family: "Open Sans", sans-serif; font-size: 24px;
  }
  .signature {
    position: absolute; left: 44px; top: 914px;
    font-family: "Alex Brush", cursive; font-size: 42px; color: #111;
  }
  .footer-band { position: absolute; left: 0; bottom: 0; width: 849px; height: 20px; display: block; }
  .website {
    position: absolute; left: 0; bottom: 1px; width: 849px; text-align: center;
    font-family: "Open Sans", sans-serif; font-size: 13.5px; line-height: 18px; color: #fff;
  }
</style>
</head>
<body>
<main class="letterhead">
  <div class="brand"><span class="brand-mark"></span>Ridgeline Builders</div>

  <address class="contact">
    <div class="address">214 Harbor View Road, Suite 9<br>Brookfield, NY 10512</div>
    <div class="line">
      <svg viewBox="0 0 10 10" aria-hidden="true"><path d="M2 0.5 L3.6 2.6 L2.7 3.6 Q3.8 5.9 6.3 7.3 L7.3 6.3 L9.5 7.9 L8.3 9.5 Q3.5 8.8 0.5 1.7 Z"/></svg>
      <span>555-214-7780</span>
    </div>
    <div class="line">
      <svg viewBox="0 0 10 10" aria-hidden="true"><path d="M0.5 2.5 H9.5 V8.5 H0.5 Z M0.5 2.5 L5 5.8 L9.5 2.5" stroke="#fff" stroke-width="0.7"/></svg>
      <span>office@ridgeline.co</span>
    </div>
  </address>

  <section class="body-copy">
    <p>Lorem ipsum dolor sit amet, consectetur adipiscing elit, sed do eiusmod tempor incididunt ut labore et dolore magna aliqua. Ut enim ad minim veniam, quis nostrud exercitation ullamco laboris nisi ut aliquip ex ea commodo consequat. Duis aute irure dolor in reprehenderit in voluptate velit esse cillum dolore eu fugiat nulla pariatur.Contrary to popular belief, Lorem Ipsum is not simply random text. It has roots in a piece of classical Latin literature from 45 BC, making it over 2000 years old. Martin Callowell, a Latin professor at Ashford-Hale College in Vermont, looked up one of the more obscure Latin words, consectetur, from a Lorem Ipsum passage, and going through the cites of the word in classical literature, discovered the undoubtable source.</p>
    <p>Lorem ipsum dolor sit amet, consectetur adipiscing elit, sed do eiusmod tempor incididunt ut labore et dolore magna aliqua. Ut enim ad minim veniam, quis nostrud exercitation ullamco laboris nisi ut aliquip ex ea commodo consequat. Duis aute irure dolor in reprehenderit in voluptate velit esse cillum dolore eu fugiat nulla pariatur. There are many variations of passages of Lorem Ipsum available, but the majority have suffered alteration in some form, by injected humour, or randomised words which don't look even slightly believable.</p>
    <p>Lorem ipsum dolor sit amet, consectetur adipiscing elit, sed do eiusmod tempor incididunt ut labore et dolore magna aliqua. Ut enim ad minim veniam, quis nostrud exercitation ullamco laboris nisi ut aliquip ex ea commodo consequat.Contrary to popular belief, Lorem Ipsum is not simply random text. It has roots in a piece of classical Latin literature from 45 BC, making it over 2000 years old. Martin Callowell, a Latin professor at Ashford-Hale College</p>
    <p>Excepteur sint occaecat cupidatat non proident, sunt in culpa qui officia deserunt mollit anim id est laborum. re et dolore magnam aliquam quaerat voluptatem.Contrary to popular belief, Lorem Ipsum is not simply random text. It has roots in a piece of classical Latin literature from 45 BC,</p>
  </section>

  <p class="closing">Sincerely,</p>
  <p class="signature">Daniel Marsh</p>

  <svg class="footer-band" viewBox="0 0 849 20" preserveAspectRatio="none" aria-hidden="true">
    <polygon points="0,0 174,0 165,20 0,20" fill="var(--ink)"/>
    <polygon points="178,0 672,0 681,20 169,20" fill="var(--orange)"/>
    <polygon points="676,0 849,0 849,20 685,20" fill="var(--ink)"/>
  </svg>
  <div class="website">www.ridgelinebuilders.com</div>
</main>
</body>
</html>
```